Create a memorable Stationary for Security Software Company

TalbrenQuay is the worldwide leader in securing the Internet. Making Internet communications and critical data secure, reliable and available everywhere has been and continues to be our ongoing vision. We are committed to staying focused on real customer needs and to developing new and innovative security solutions that redefine the security landscape.

Industry/Entity Type

Internet

Font styles to use
Serif
Sans Serif
Script

Colors
0792cd
33a6d7
85cae6

```html
<!DOCTYPE html>
<html lang="en">
<head>
<meta charset="UTF-8">
<title>TalbrenQuay Business Card</title>
<link href="https://fonts.googleapis.com/css2?family=Ubuntu:wght@400;500&display=swap" rel="stylesheet">
<style>
  :root {
    --page-bg: #d9d4cc;
    --brand-deep: #0a6fb8;
    --brand-main: #0792cd;
    --brand-mid: #33a6d7;
    --brand-light: #85cae6;
    --frost: #e9eef1;
    --frost-edge: #cdd6dc;
    --text-light: #eef6fb;
    --text-muted: #a9d3e8;
  }
  * { margin: 0; padding: 0; box-sizing: border-box; }
  html, body {
    width: 1200px;
    height: 970px;
    overflow: hidden;
    background: var(--page-bg);
    font-family: "Ubuntu", sans-serif;
  }
  .card {
    position: absolute;
    left: 100px;
    top: 201px;
    width: 1000px;
    height: 567px;
    border-radius: 22px;
    overflow: hidden;
    background: linear-gradient(160deg, var(--frost) 0%, #dfe6ea 100%);
    box-shadow: 0 0 0 1px var(--frost-edge);
  }
  .card-band {
    position: absolute;
    inset: 0;
    width: 1000px;
    height: 567px;
  }
  .card-details {
    position: absolute;
    left: 53px;
    top: 88px;
    color: var(--text-light);
  }
  .employee-name { font-size: 34px; font-weight: 400; line-height: 1.05; }
  .employee-title { font-size: 25px; color: var(--text-muted); line-height: 1.1; }
  .address {
    margin-top: 88px;
    font-size: 26px;
    line-height: 1.3;
  }
  .contact-list {
    list-style: none;
    margin-top: 26px;
    font-size: 27px;
    line-height: 1.28;
  }
  .contact-list li { display: flex; align-items: center; gap: 9px; }
  .contact-icon { width: 26px; height: 26px; flex: none; }
  .website {
    margin-top: 30px;
    font-size: 23px;
    color: var(--text-muted);
  }
  .brand {
    position: absolute;
    left: 590px;
    top: 254px;
    display: flex;
    align-items: center;
    gap: 14px;
    color: var(--brand-main);
    font-size: 38px;
    font-weight: 500;
  }
  .brand-dot {
    width: 30px;
    height: 30px;
    border-radius: 50%;
    background: var(--brand-main);
  }
</style>
</head>
<body>
  <div class="card">
    <svg class="card-band" viewBox="0 0 1000 567" aria-hidden="true">
      <defs>
        <linearGradient id="band-fill" x1="0" y1="0" x2="1" y2="1">
          <stop offset="0" stop-color="#1f8fc9"/>
          <stop offset="0.55" stop-color="#0792cd"/>
          <stop offset="1" stop-color="#0a6fb8"/>
        </linearGradient>
      </defs>
      <path d="M0 0 H495 Q410 283 495 567 H0 Z" fill="url(#band-fill)"/>
      <path d="M495 0 Q410 283 495 567" fill="none" stroke="#85cae6" stroke-width="3" opacity="0.8"/>
      <path d="M478 0 Q395 283 478 567" fill="none" stroke="#33a6d7" stroke-width="2" opacity="0.6"/>
    </svg>

    <div class="card-details">
      <p class="employee-name">Employee Name</p>
      <p class="employee-title">President</p>
      <p class="address">0000 Youe Address,2nd Ste.<br>Lindcrest, Avora 1234</p>
      <ul class="contact-list">
        <li>
          <svg class="contact-icon" viewBox="0 0 26 26" aria-label="Phone">
            <rect x="1" y="1" width="24" height="24" rx="3" fill="#85cae6" opacity="0.6"/>
            <path d="M6 10 Q13 4 20 10 L18 12 L15 10 L11 10 L8 12 Z M8 14 H18 V20 H8 Z" fill="#0a6fb8"/>
          </svg>
          +000-000-0000
        </li>
        <li>
          <svg class="contact-icon" viewBox="0 0 26 26" aria-label="Fax">
            <rect x="1" y="1" width="24" height="24" rx="3" fill="#85cae6" opacity="0.6"/>
            <rect x="8" y="5" width="10" height="6" fill="#0a6fb8"/>
            <rect x="5" y="11" width="16" height="7" rx="1" fill="#0a6fb8"/>
            <rect x="8" y="16" width="10" height="5" fill="#eef6fb"/>
          </svg>
          123 456 7890
        </li>
        <li>
          <svg class="contact-icon" viewBox="0 0 26 26" aria-label="Email">
            <rect x="1" y="1" width="24" height="24" rx="3" fill="#85cae6" opacity="0.6"/>
            <rect x="5" y="7" width="16" height="12" fill="none" stroke="#0a6fb8" stroke-width="1.6"/>
            <path d="M5 7 L13 14 L21 7 M5 19 L11 13 M21 19 L15 13" fill="none" stroke="#0a6fb8" stroke-width="1.6"/>
          </svg>
          your@yourcompany.com
        </li>
      </ul>
      <p class="website">www.yourcompany.com</p>
    </div>

    <div class="brand">
      <span class="brand-dot"></span>
      <span class="brand-name">TalbrenQuay</span>
    </div>
  </div>
</body>
</html>
```